Cloud-based Health 2.0 Web Site

We need the overall look and feel for a new cloud-based Health 2.0 web site where health professionals can manage and interact with their patients/clients.

The plan is to generate a landing page that can grab the attention of health professionals (doctors, nurses, personal trainers, etc...). This page should have an attractive "Sign Up for Free" or similar button/message, as well as a login section for users already registered. We currently have a view on having a number of messages displayed, either as a slider or as separate areas on the page (decision is up for grabs).

Secondly, we need a standard "framework" for all the other pages which will be accessible once the user has authenticated with a clean, airy and spacious feel. This will provide styling for standard elements (input boxes, checkboxes, etc...) as well as a given layout, possibly 3 columns (fixed-fluid-fixed) although we leave this to the designer's choice.

We want to stress the importance of the Cloud, as well as make users feel like "this is the place to be if you're a modern, tech savvy health professional". Also of high importance is to show that this is a secure place, where data is accessible from anywhere yet also highly protected.

This project is going to provide long-term work for the winner and possibly those we consider close runner ups, so if you guys are interested in grabbing our attention so you can become our designer of choice, this is your chance!

Standard pages we are looking to receive after the selection process:

* Landing page
* Health Professional Profile Page (personal details, professional details, photo...)
* Patient list / Patient Management page
* Patient profile (details, health details...)
* Generic "item" management page (item refers to documents, images, contacts, etc...)

The logo for the site/product is also up for grabs, and a bonus payment can be given if you provide one that both matches the style of the site whilst being one that could be reused for mobile app icons, etc...
Updates

The site name is "vireplank" (all lower-case) for those of you wanting to work on the logo part. As I said before, the logo should contain a component that could be use as the recognisable icon in a mobile phone app. Something that can be easily identified in both the site and the app that connects them together.

vireplank is made up of two parts (vire + plank), and you might want to consider differentiating them by the use of colour, fonts or however you think appropriate.

New sample screen-shots of the existing functionality have been uploaded to help you mock up some screens.

PLEASE NOTE: This are to be used for content/widget design only! The layout of how these are represented, e.g. accordion, slider, tree, list... is entirely up to you! Don't guide your layout based on these screen-shots, unless you think they are the way to go, of course. 

We want your creative input, so please innovate! :)

Thanks!

Target Market(s)

Health Professionals

Industry/Entity Type

Health

Requirements
Must have
• * A landing page that grabs the users attention but is "different" from the rest of pages (although within the same design/style parameters)

* A generic page framework for the rest of the pages (style guide)
Nice to have
• A modern and clean logo to go with the site. If the logo is selected, this can result in a bonus payment to be decided.

```html
<!DOCTYPE html>
<html lang="en">
<head>
<meta charset="utf-8">
<title>vireplank – the ultimate platform for health care professionals</title>
<link rel="stylesheet" href="https://fonts.googleapis.com/css2?family=Ubuntu:wght@400;500;700&family=Arimo:wght@400;700&display=swap">
<style>
:root{
  --sky-top:#a9cdee;
  --sky-mid:#cfe4f7;
  --sky-low:#eef6fd;
  --brand-green:#8cc63f;
  --brand-blue:#1a9ad6;
  --panel-top:#1aa3e3;
  --panel-bottom:#0a4f9e;
  --cta-top:#9bd21c;
  --cta-bottom:#4f9a0f;
  --ink:#222;
  --ink-soft:#555;
  --ink-muted:#8a8a8a;
  --link-blue:#1a8fd6;
  --rule:#b8b8b8;
  --footer-top:#7a7a7a;
  --footer-bottom:#2d2d2d;
  --white:#fff;
}
*{box-sizing:border-box;margin:0;padding:0}
html,body{width:1200px;height:1117px;overflow:hidden}
body{position:relative;background:var(--white);font-family:"Arimo",Arial,sans-serif;color:var(--ink)}
.sky{position:absolute;left:0;top:0;width:1200px;height:570px;
  background:radial-gradient(ellipse at 50% 30%,rgba(255,255,255,.75),rgba(255,255,255,0) 60%),
  linear-gradient(to bottom,var(--sky-top) 0%,var(--sky-mid) 55%,var(--sky-low) 85%,var(--white) 100%)}
.logo{position:absolute;left:168px;top:38px;display:flex;align-items:center;gap:10px}
.logo-mark{width:16px;height:16px;border-radius:50%;background:var(--brand-blue)}
.logo-name{font-family:"Ubuntu",sans-serif;font-weight:700;font-size:34px;color:var(--brand-blue);letter-spacing:1px}
.main-nav{position:absolute;top:19px;left:512px;display:flex;align-items:center;font-family:"Ubuntu",sans-serif;font-size:12px;color:var(--ink)}
.main-nav a{color:var(--ink);text-decoration:none}
.main-nav .current{display:inline-block;width:82px;height:31px;line-height:29px;text-align:center;border:2px solid var(--white);border-radius:7px;background:linear-gradient(#f7f7f7,#d9d9d9);box-shadow:0 1px 3px rgba(0,0,0,.25)}
.main-nav .sep{margin:0 38px 0 18px}
.account{position:absolute;top:90px;left:890px;display:flex;gap:10px}
.account a{display:block;height:24px;line-height:24px;padding:0 12px;font-family:"Ubuntu",sans-serif;font-size:12px;color:#444;text-decoration:none;border-radius:5px;background:linear-gradient(#fff,#dcdcdc);box-shadow:0 1px 2px rgba(0,0,0,.2)}
.account .login{width:66px;text-align:center}
.account .signup{width:98px;text-align:center}
.hero{position:absolute;left:133px;top:131px;width:934px;height:388px;background:var(--white);border:1px solid #e0e6ec}
.hero-shadow{position:absolute;left:150px;top:520px;width:900px;height:14px;background:radial-gradient(ellipse at 50% 0,rgba(0,0,0,.28),rgba(0,0,0,0) 70%)}
.hero-photo{position:absolute;left:10px;top:9px;width:613px;height:369px;background:linear-gradient(90deg,#cfd9dd 0%,#8fb7ad 30%,#86a9c4 60%,#3c7fc0 90%,#2a6aa6 100%)}
.hero-panel{position:absolute;left:627px;top:10px;width:294px;height:362px;background:linear-gradient(to bottom,var(--panel-top),var(--panel-bottom));color:var(--white);padding:24px 14px 0 14px;font-family:"Ubuntu",sans-serif}
.hero-title{font-size:21px;line-height:29px;font-weight:400}
.hero-title strong{font-weight:700}
.hero-text{margin-top:22px;font-size:16px;line-height:23px}
.cta{position:absolute;left:648px;top:334px;width:250px;height:51px;border-radius:4px;background:linear-gradient(to bottom,var(--cta-top),var(--cta-bottom));color:var(--white);font-family:"Ubuntu",sans-serif;font-weight:700;font-size:24px;line-height:51px;text-align:center;text-decoration:none;box-shadow:0 2px 3px rgba(0,0,0,.25)}
.cta strong{font-size:28px}
.slide-arrow{position:absolute;top:278px;width:40px;height:92px}
.slide-arrow.prev{left:122px}
.slide-arrow.next{left:1037px}
.col-title{position:absolute;font-family:"Ubuntu",sans-serif;font-size:20px;color:var(--ink-soft);font-weight:400}
.col-title strong{color:var(--brand-blue);font-weight:700}
.about-icon{position:absolute;left:139px;top:604px}
.about-title{left:183px;top:603px}
.about-photo{position:absolute;left:163px;top:643px;width:231px;height:221px;background:radial-gradient(ellipse at 50% 45%,#6fa7df 0%,#9cc6ec 45%,#ffffff 78%)}
.about-text{position:absolute;left:153px;top:880px;width:289px;font-size:12px;line-height:19.2px;text-align:justify;color:#333;letter-spacing:.3px}
.about-text strong{color:var(--ink)}
.divider{position:absolute;top:630px;width:0;height:360px;border-left:1px dotted #999}
.msg-icon{position:absolute;left:480px;top:598px}
.msg-title{left:533px;top:607px}
.messages{position:absolute;left:482px;top:655px;width:290px;list-style:none}
.message{font-size:12px;line-height:19.2px;text-align:justify;letter-spacing:.3px;color:#333;padding-bottom:14px;margin-bottom:14px;border-bottom:1px dotted #999}
.message b{color:var(--ink)}
.message .time{color:var(--link-blue)}
.login-box{position:absolute;left:802px;top:614px;width:258px;height:137px;border:2px solid #e3e3e3;border-radius:8px;background:linear-gradient(#fff,#ececec);padding:10px 12px}
.login-box h3{font-family:"Ubuntu",sans-serif;font-size:18px;font-weight:500;color:#555}
.field{display:flex;align-items:center;margin-top:9px;font-size:11px;color:var(--ink-muted);letter-spacing:.6px}
.field label{width:66px}
.field input{width:164px;height:23px;border:1px solid #c8c8c8;border-radius:7px;background:var(--white)}
.login-btn{position:absolute;right:26px;bottom:8px;width:56px;height:22px;border:0;border-radius:5px;background:linear-gradient(#2a9be0,#0a5ea8);color:var(--white);font-family:"Ubuntu",sans-serif;font-size:12px}
.login-shadow{position:absolute;left:820px;top:752px;width:220px;height:10px;background:radial-gradient(ellipse at 50% 0,rgba(0,0,0,.25),rgba(0,0,0,0) 70%)}
.follow-banner{position:absolute;left:799px;top:783px;width:217px;height:43px;background:linear-gradient(#3a3a3a,#1c1c1c);display:flex;align-items:center;gap:12px;padding-left:10px;font-family:"Ubuntu",sans-serif;font-size:16px;color:var(--white)}
.follow-banner span.dot{width:30px;height:30px;border-radius:50%;background:#4db3ea}
.social{position:absolute;left:806px;top:840px;list-style:none}
.social li{display:flex;align-items:center;height:39.3px;font-family:"Ubuntu",sans-serif;font-size:15px;color:#777}
.social .badge{width:30px;height:30px;border-radius:50%;margin-right:12px;box-shadow:0 1px 2px rgba(0,0,0,.3)}
.badge.b1{background:radial-gradient(circle at 35% 30%,#6c8fd4,#2a4f9c)}
.badge.b2{background:radial-gradient(circle at 35% 30%,#5fb3de,#1c6d9c)}
.badge.b3{background:radial-gradient(circle at 35% 30%,#aee3f3,#3ea9cf)}
.badge.b4{background:radial-gradient(circle at 35% 30%,#e36a6a,#a41b1b)}
.col-shadow{position:absolute;top:1010px;width:310px;height:14px;background:radial-gradient(ellipse at 50% 0,rgba(0,0,0,.3),rgba(0,0,0,0) 70%)}
.footer{position:absolute;left:0;top:1058px;width:1200px;height:59px;background:linear-gradient(var(--footer-top),var(--footer-bottom));display:flex;justify-content:center;align-items:center;font-family:"Ubuntu",sans-serif;font-size:12px;color:var(--white)}
.footer a{color:var(--white);text-decoration:none}
.footer .sep{margin:0 16px}
</style>
</head>
<body>
<div class="sky"></div>

<header>
  <div class="logo"><span class="logo-name">VIREPLANK</span><span class="logo-mark"></span></div>
  <nav class="main-nav">
    <a class="current" href="#">About us</a><span class="sep" style="margin-left:18px">|</span>
    <a href="#">solutions</a><span class="sep">|</span>
    <a href="#">Services</a><span class="sep">|</span>
    <a href="#">News &amp; Events</a><span class="sep">|</span>
    <a href="#">Contact us</a>
  </nav>
  <div class="account"><a class="login" href="#">Login</a><a class="signup" href="#">Sign Up Now</a></div>
</header>

<section class="hero">
  <div class="hero-photo" role="img" aria-label="Photo of a team of doctors and nurses in scrubs standing in a hospital corridor"></div>
  <div class="hero-panel">
    <h1 class="hero-title"><strong>THE ULTIMATE PLATFORM</strong> for health care professionals and <strong>PATIENTS</strong> to meet in the cloud</h1>
    <p class="hero-text">Have you found the question-naire you were looking for but not in your language? Translate it yourself and make it available to the community.</p>
  </div>
  <a class="cta" href="#">Start <strong>Free</strong> Sign Up</a>
</section>
<div class="hero-shadow"></div>

<svg class="slide-arrow prev" viewBox="0 0 40 92" aria-label="Previous slide">
  <path d="M40 0 C10 12 0 30 0 46 C0 62 10 80 40 92 Z" fill="#f4f6f8" stroke="#c9d2da"/>
  <path d="M8 46 L22 32 L22 40 L32 40 L32 52 L22 52 L22 60 Z" fill="#1a7fd0"/>
</svg>
<svg class="slide-arrow next" viewBox="0 0 40 92" aria-label="Next slide">
  <path d="M0 0 C30 12 40 30 40 46 C40 62 30 80 0 92 Z" fill="#f4f6f8" stroke="#c9d2da"/>
  <path d="M32 46 L18 32 L18 40 L8 40 L8 52 L18 52 L18 60 Z" fill="#1a7fd0"/>
</svg>

<main>
  <svg class="about-icon" width="36" height="36" viewBox="0 0 36 36" aria-hidden="true">
    <path d="M2 3 H34 V25 H14 L7 33 V25 H2 Z" fill="#fff" stroke="#1a7fd0" stroke-width="2.5" stroke-linejoin="round"/>
    <path d="M8 10 H28 M8 15 H28 M8 20 H22" stroke="#222" stroke-width="2"/>
  </svg>
  <h2 class="col-title about-title">About <strong>VirePlank</strong></h2>
  <div class="about-photo" role="img" aria-label="Photo of a smiling medical team with a doctor in a white coat"></div>
  <p class="about-text"><strong>Applying new technologies to solve the problem of health management has</strong> been the dream of many for a long time. With today's technology we are closer than ever to achieve this dream, and vireplank rep-resents a collection of unique technologies and ideas that will revolutionaise .</p>

  <div class="divider" style="left:461px"></div>

  <svg class="msg-icon" width="42" height="40" viewBox="0 0 42 40" aria-hidden="true">
    <rect x="8" y="4" width="24" height="20" fill="#fff" stroke="#6aa9dc" transform="rotate(-10 20 14)"/>
    <path d="M2 16 L21 30 L40 16 V38 H2 Z" fill="#f6b21a" stroke="#d48a00"/>
    <path d="M2 38 L17 27 M40 38 L25 27" stroke="#d48a00"/>
  </svg>
  <h2 class="col-title msg-title">New <strong>Messages</strong></h2>
  <ul class="messages">
    <li class="message"><b>RT @MediaLedger:</b> Northgate Press develops person-alised content withpersonalised content with Tastemap Labs http://ln.ko/8Qm41Zx<br><span class="time">(13 hours ago )</span></li>
    <li class="message"><b>RT @MediaLedger:</b> Northgate Press develops person-alised content withpersonalised content with Tastemap Labs http://ln.ko/8Qm41Zx<br><span class="time">(13 hours ago )</span></li>
    <li class="message"><b>RT @MediaLedger:</b> Northgate Press develops person-alised content withpersonalised Northgate Press develops personalised content withpersonalised content withcontent with Tastemap Labs http://ln.ko/8Qm41Zx<br><span class="time">(13 hours ago )</span></li>
  </ul>

  <div class="divider" style="left:782px"></div>

  <form class="login-box">
    <h3>Login Area</h3>
    <div class="field"><label>Username</label><input type="text"></div>
    <div class="field"><label>Password</label><input type="password"></div>
    <button class="login-btn" type="button">Login</button>
  </form>
  <div class="login-shadow"></div>

  <div class="follow-banner"><span class="dot"></span>Follow Us on Chirper</div>
  <ul class="social">
    <li><span class="badge b1"></span>Follow us on Circlebook</li>
    <li><span class="badge b2"></span>Follow us on Worklinker</li>
    <li><span class="badge b3"></span>Follow us on Chirper</li>
    <li><span class="badge b4"></span>Follow us on Viewtube</li>
  </ul>

  <div class="col-shadow" style="left:150px"></div>
  <div class="col-shadow" style="left:470px"></div>
  <div class="col-shadow" style="left:790px"></div>
</main>

<footer class="footer">
  <a href="#">About us</a><span class="sep" style="margin-left:6px">|</span>
  <a href="#">Products &amp; solutions</a><span class="sep">|</span>
  <a href="#">Services</a><span class="sep">|</span>
  <a href="#">News &amp; Events</a><span class="sep">|</span>
  <a href="#">Regulatory &amp; Scientific</a>
</footer>
</body>
</html>
```